Premium Skincare Packaging Design for Vale Hollow

Vale Hollow (https://valehollow-example.com) is a premium wellness brand from Canada specializing in beef tallow (for cooking) and now expanding into natural skincare. We are seeking packaging design concepts for two new 60 ml skincare products made with grass-fed beef tallow.
Our goal is to achieve a clean, minimalist yet luxurious look that reflects purity, quality and sophistication. The design should look premium enough for high-end skincare shelves while maintaining a natural, grounded feel.
You will be designing:
- Jar label (wrap-around design) for a 60 ml glass jar with black lid
- Round lid sticker (for the top of the black lid)
- Square outer box (for each jar)
- Both products are very similar, so the differentiation can be minimal.

Products to Design
1. All-Purpose Tallow Balm
Jar: Frosted glass, 60 ml with black lid
Purpose: Moisturizer for face, lips, hands, and body
Ingredients: Grass-fed beef tallow, beeswax, honey, vitamin E
Tone: Natural, pure, versatile, gentle
Tagline: “Crafted from nature’s simplest elements”
Preferred color palette:
Light / off-white background
Beige and honey accents
Black or dark brown typography
Mood: Minimalist apothecary meets warm, natural simplicity
2. Face Tallow Cream
Purpose: Face moisturizer with nourishing tallow and botanicals
Tone: Refined, elegant, modern, premium
Tagline: “The strength of tallow, refined for your face”
Preferred color palette:
Deep charcoal or black background
Gold or cream typography
Accent in subtle metallic tones (gold or bronze)
Mood: Modern luxury with understated confidence
Design Deliverables
For each product, submit:
1) Jar Label (Wrap-around)
- Include product name, logo, tagline, ingredients, and size (60 ml / 2 fl oz).
- Space for barcode and manufacturing details (leave placeholder).
2) Round Lid Sticker
- Centered logo and minimalist border or accent ring.
3) Outer Paper Box (Square)
- Matching color palette and typography.
- Clean layout featuring the Vale Hollow logo and tagline.
- Text to include: product name, tagline, ingredients and size.

Brand Guidelines
Logo: Use the existing Vale Hollow logo (we’ll upload it for reference).
Typography: Clean and elegant — sans-serif or classic serif fonts.
Tone: Pure, premium, and intentional — less is more.
Design cohesion: Both products must look like part of one collection.

```html
<!DOCTYPE html>
<html lang="en">
<head>
<meta charset="utf-8">
<title>Vale Hollow – All-Purpose Tallow Balm Packaging</title>
<link rel="stylesheet" href="https://fonts.googleapis.com/css2?family=Jost:wght@400;500&family=EB+Garamond:ital@1&display=swap">
<style>
  :root {
    --paper: #ffffff;
    --cream: #f5f3ec;
    --beige: #c8bca6;
    --mist: #ccd6d6;
    --band: #c3cdcd;
    --lid: #2a2a2a;
    --ink-brown: #6a5342;
    --ink-grey: #7b7c79;
    --rule: #a9aaa6;
  }
  * { box-sizing: border-box; margin: 0; padding: 0; }
  html, body { width: 1200px; height: 1200px; overflow: hidden; background: var(--paper); }
  body { position: relative; font-family: "Jost", sans-serif; color: var(--ink-brown); }

  .panel { position: absolute; }
  .panel svg.art { position: absolute; inset: 0; width: 100%; height: 100%; display: block; }
  .panel .copy { position: absolute; inset: 0; text-align: center; }

  .brand { position: absolute; left: 0; right: 0; display: flex; align-items: center; justify-content: center; gap: 6px;
           font-weight: 500; color: var(--ink-brown); letter-spacing: 0.06em; white-space: nowrap; }
  .brand-square { display: inline-block; background: var(--ink-brown); }

  .title { position: absolute; left: 0; right: 0; font-weight: 500; white-space: nowrap; letter-spacing: 0.01em; }
  .subtitle { position: absolute; left: 0; right: 0; color: var(--ink-grey); white-space: nowrap; letter-spacing: 0.02em; }
  .ingredients { position: absolute; color: var(--ink-grey); white-space: nowrap; text-align: center;
                 border-top: 1px solid var(--rule); border-bottom: 1px solid var(--rule); }
  .tagline { position: absolute; left: 0; right: 0; font-family: "EB Garamond", serif; font-style: italic; color: var(--ink-grey); white-space: nowrap; }
  .size { position: absolute; left: 0; right: 0; color: #3d3a36; white-space: nowrap; }

  /* Round lid sticker */
  .lid-sticker { left: 164px; top: 149px; width: 356px; height: 356px; }
  .lid-sticker .brand { top: 120px; font-size: 15px; }
  .lid-sticker .brand-square { width: 10px; height: 10px; }
  .lid-sticker .title { top: 178px; font-size: 22px; }
  .lid-sticker .subtitle { top: 205px; font-size: 13px; }

  /* Lid side band */
  .lid-band { left: 126px; top: 568px; width: 422px; height: 78px; background: var(--band);
              border-top: 12px solid var(--lid); display: flex; align-items: center; overflow: hidden; }
  .lid-band .repeat { white-space: nowrap; font-size: 17px; font-weight: 500; color: var(--ink-brown); margin-left: -8px; letter-spacing: 0.01em; }

  /* Wrap-around jar label */
  .jar-label { left: 126px; top: 680px; width: 422px; height: 230px; }
  .jar-label .brand { top: 28px; font-size: 16px; }
  .jar-label .brand-square { width: 11px; height: 11px; }
  .jar-label .title { top: 78px; font-size: 25px; }
  .jar-label .subtitle { top: 110px; font-size: 14.5px; }
  .jar-label .ingredients { left: 68px; right: 68px; top: 134px; height: 24px; line-height: 22px; font-size: 11px; }
  .jar-label .tagline { top: 164px; font-size: 12.5px; }
  .jar-label .size { top: 203px; font-size: 12px; }

  /* Outer box front */
  .box-front { left: 640px; top: 300px; width: 440px; height: 440px; background: var(--mist); }
  .box-label { left: 105px; top: 105px; width: 230px; height: 230px; }
  .box-label .brand { top: 52px; font-size: 11px; }
  .box-label .brand-square { width: 7px; height: 7px; }
  .box-label .title { top: 88px; font-size: 15px; }
  .box-label .subtitle { top: 109px; font-size: 8.5px; }
  .box-label .ingredients { left: 14px; right: 14px; top: 125px; height: 16px; line-height: 14px; font-size: 7px; }
  .box-label .tagline { top: 146px; font-size: 8px; }
  .box-label .size { top: 198px; font-size: 8px; }
</style>
</head>
<body>

  <!-- Round lid sticker -->
  <section class="panel lid-sticker" aria-label="Round lid sticker">
    <svg class="art" viewBox="0 0 356 356" aria-hidden="true">
      <defs><clipPath id="sticker-clip"><circle cx="178" cy="178" r="178"/></clipPath></defs>
      <g clip-path="url(#sticker-clip)">
        <rect width="356" height="356" fill="var(--cream)"/>
        <path d="M0 0 H203 C175 70 150 150 95 180 C60 200 25 215 0 222 Z" fill="var(--beige)"/>
        <path d="M330 80 C300 140 250 180 225 230 C210 270 205 320 205 356 H356 V60 Z" fill="var(--mist)"/>
      </g>
    </svg>
    <div class="copy">
      <div class="brand"><span class="brand-square"></span>Vale Hollow</div>
      <div class="title">All-Purpose Tallow Balm</div>
      <div class="subtitle">Moisturizer for Face, Lips, Hands &amp; Body</div>
    </div>
  </section>

  <!-- Lid side band -->
  <section class="panel lid-band" aria-label="Lid side band">
    <div class="repeat">All-Purpose Tallow Balm &nbsp;•&nbsp; All-Purpose Tallow Balm &nbsp;•&nbsp; All-Purpose Tallow Balm</div>
  </section>

  <!-- Jar wrap label -->
  <section class="panel jar-label" aria-label="Jar label">
    <svg class="art" viewBox="0 0 422 230" preserveAspectRatio="none" aria-hidden="true">
      <rect width="422" height="190" fill="var(--cream)"/>
      <path d="M0 0 H365 C320 60 250 110 170 140 C110 160 50 175 0 185 Z" fill="var(--beige)"/>
      <path d="M422 20 C395 70 375 120 355 190 H422 Z" fill="var(--mist)"/>
      <rect y="190" width="422" height="40" fill="var(--band)"/>
    </svg>
    <div class="copy">
      <div class="brand"><span class="brand-square"></span>Vale Hollow</div>
      <div class="title">All-Purpose Tallow Balm</div>
      <div class="subtitle">Moisturizer for Face, Lips, Hands &amp; Body</div>
      <div class="ingredients">With Grass-fed Beef Tallow, Beeswax, Honey &amp; Vitamin E</div>
      <div class="tagline">Crafted from Nature’s Simplest Elements</div>
      <div class="size">60 ml</div>
    </div>
  </section>

  <!-- Outer box front face -->
  <section class="panel box-front" aria-label="Outer box front">
    <div class="panel box-label">
      <svg class="art" viewBox="0 0 230 230" aria-hidden="true">
        <rect width="230" height="230" fill="var(--cream)"/>
        <path d="M0 0 H205 C185 50 150 80 105 100 C70 115 30 122 0 130 Z" fill="var(--beige)"/>
        <path d="M230 70 C205 110 190 150 185 230 H230 Z" fill="var(--mist)"/>
      </svg>
      <div class="copy">
        <div class="brand"><span class="brand-square"></span>Vale Hollow</div>
        <div class="title">All-Purpose Tallow Balm</div>
        <div class="subtitle">Moisturizer for Face, Lips, Hands &amp; Body</div>
        <div class="ingredients">With Grass-fed Beef Tallow, Beeswax, Honey &amp; Vitamin E</div>
        <div class="tagline">Crafted from Nature’s Simplest Elements</div>
        <div class="size">60 ml</div>
      </div>
    </div>
  </section>

</body>
</html>
```